Assorted Banner Ads

Create standard sized banner ads (300x250, 728x90, 160x600) using logo and create exciting ads using collateral provided and your own ideas.

```html
<!DOCTYPE html>
<html lang="en">
<head>
<meta charset="utf-8">
<title>Harbor Lane Room Escape – Banner Set</title>
<link rel="stylesheet" href="https://fonts.googleapis.com/css2?family=Josefin+Sans:wght@700&family=Oswald:wght@400&family=Open+Sans:wght@400&display=swap">
<style>
  :root {
    --board: #353130;
    --board-dark: #2c2827;
    --brand-green: #2e7d3c;
    --edge-dark: #262626;
    --paper: #ffffff;
    --ink: #2a2a2a;
    --label: #e6e6e6;
    --photo-deep: #5a2f12;
    --photo-mid: #b8702a;
    --photo-light: #e9b86a;
  }
  * { margin: 0; padding: 0; box-sizing: border-box; }
  html, body { width: 1200px; height: 1200px; overflow: hidden; background: var(--board); }
  .stage {
    position: relative; width: 960px; height: 960px;
    transform: scale(1.25); transform-origin: 0 0;
    background: linear-gradient(90deg, var(--board-dark), var(--board) 50%, var(--board-dark));
  }
  .stage-rule { position: absolute; left: 0; width: 960px; height: 7px; background: var(--brand-green); }
  .stage-rule.top { top: 0; }
  .stage-rule.bottom { bottom: 0; height: 8px; }
  .size-label {
    position: absolute; font-family: "Open Sans", sans-serif; font-size: 15px; color: var(--label);
  }
  .banner { position: absolute; overflow: hidden; background: var(--paper); box-shadow: 0 2px 8px rgba(0,0,0,.45); }
  .banner svg.shapes { position: absolute; inset: 0; }
  .headline {
    position: absolute; font-family: "Josefin Sans", sans-serif; font-weight: 700;
    color: var(--paper); line-height: 1.22;
  }
  .tagline {
    position: absolute; font-family: "Oswald", sans-serif; font-weight: 400;
    color: var(--paper); line-height: 1.3;
  }
  .brand { position: absolute; display: flex; flex-direction: column; align-items: center; }
  .brand-square { width: 22px; height: 22px; background: var(--brand-green); margin-bottom: 6px; }
  .brand-name, .brand-sub {
    font-family: "Josefin Sans", sans-serif; font-weight: 700; color: var(--ink);
    letter-spacing: 1px; line-height: 1.1; white-space: nowrap;
  }
  .brand-name { font-size: 13px; }
  .brand-sub { font-size: 8px; letter-spacing: 2px; margin-top: 2px; }
  .cta {
    position: absolute; background: var(--brand-green); color: var(--paper);
    font-family: "Josefin Sans", sans-serif; font-weight: 700; font-size: 15px;
    display: flex; align-items: center; justify-content: center; padding-top: 3px;
  }
</style>
</head>
<body>
<div class="stage">
  <div class="stage-rule top"></div>

  <!-- Leaderboard 728 x 90 -->
  <div class="size-label" style="left:117px;top:77px;">728-90</div>
  <div class="banner leaderboard" style="left:116px;top:116px;width:728px;height:90px;">
    <svg class="shapes" width="728" height="90" viewBox="0 0 728 90">
      <defs>
        <linearGradient id="photoWide" x1="0" y1="0" x2="1" y2="1">
          <stop offset="0" stop-color="var(--photo-deep)"/>
          <stop offset=".45" stop-color="var(--photo-light)"/>
          <stop offset="1" stop-color="var(--photo-mid)"/>
        </linearGradient>
      </defs>
      <polygon points="0,0 205,0 220,45 205,90 0,90" fill="var(--brand-green)"/>
      <polygon points="205,0 485,0 500,45 485,90 205,90 220,45" fill="var(--edge-dark)"/>
      <polygon points="214,0 478,0 493,45 478,90 214,90 229,45" fill="url(#photoWide)" role="img" aria-label="Photo of a wooden ship-cabin escape room with a desk and globe"/>
    </svg>
    <div class="headline" style="left:19px;top:12px;font-size:20px;">Can you Escape<br>in 60 Minutes?</div>
    <div class="tagline" style="left:17px;top:60px;font-size:14px;">Find Clues! Slove Puzzels!</div>
    <div class="brand" style="left:508px;top:10px;width:100px;">
      <div class="brand-square"></div>
      <div class="brand-name">HARBOR LANE</div>
      <div class="brand-sub">ROOM ESCAPE</div>
    </div>
    <div class="cta" style="left:616px;top:37px;width:104px;height:28px;">Read More</div>
  </div>

  <!-- Medium rectangle 300 x 250 -->
  <div class="size-label" style="left:117px;top:243px;">300-250</div>
  <div class="banner rectangle" style="left:116px;top:276px;width:300px;height:250px;">
    <svg class="shapes" width="300" height="250" viewBox="0 0 300 250">
      <defs>
        <linearGradient id="photoRect" x1="0" y1="0" x2="0" y2="1">
          <stop offset="0" stop-color="var(--photo-mid)"/>
          <stop offset=".45" stop-color="var(--photo-light)"/>
          <stop offset="1" stop-color="var(--photo-deep)"/>
        </linearGradient>
      </defs>
      <polygon points="0,0 210,0 140,127 0,127" fill="var(--brand-green)"/>
      <polygon points="210,0 300,0 300,250 192,250 132,127" fill="var(--edge-dark)"/>
      <polygon points="218,0 300,0 300,250 201,250 142,127" fill="url(#photoRect)" role="img" aria-label="Photo of a wooden ship-cabin escape room with a desk and globe"/>
    </svg>
    <div class="headline" style="left:8px;top:24px;font-size:19px;">Can you Escape<br>in 60 Minutes?</div>
    <div class="tagline" style="left:7px;top:71px;font-size:16px;">Find Clues! Slove Puzzels!</div>
    <div class="brand" style="left:25px;top:134px;width:100px;">
      <div class="brand-square"></div>
      <div class="brand-name">HARBOR LANE</div>
      <div class="brand-sub">ROOM ESCAPE</div>
    </div>
    <div class="cta" style="left:21px;top:213px;width:113px;height:29px;">Read More</div>
  </div>

  <!-- Skyscraper 160 x 600 -->
  <div class="size-label" style="left:477px;top:244px;">160-600</div>
  <div class="banner skyscraper" style="left:480px;top:276px;width:160px;height:600px;">
    <svg class="shapes" width="160" height="600" viewBox="0 0 160 600">
      <defs>
        <linearGradient id="photoTall" x1="0" y1="0" x2="0" y2="1">
          <stop offset="0" stop-color="var(--photo-deep)"/>
          <stop offset=".35" stop-color="var(--photo-light)"/>
          <stop offset=".7" stop-color="var(--photo-mid)"/>
          <stop offset="1" stop-color="var(--photo-deep)"/>
        </linearGradient>
      </defs>
      <polygon points="0,0 160,0 160,199 80,159 0,199" fill="var(--brand-green)"/>
      <polygon points="0,192 80,152 160,192 160,425 80,465 0,425" fill="var(--edge-dark)"/>
      <polygon points="0,199 80,159 160,199 160,418 80,458 0,418" fill="url(#photoTall)" role="img" aria-label="Photo of a wooden ship-cabin escape room with a desk and globe"/>
    </svg>
    <div class="headline" style="left:0;top:20px;width:160px;text-align:center;font-size:22px;line-height:1.15;">Can you<br>Escape in 60<br>Minutes?</div>
    <div class="tagline" style="left:0;top:96px;width:160px;text-align:center;font-size:17px;">Find Clues!<br>Slove Puzzels!</div>
    <div class="brand" style="left:30px;top:480px;width:100px;">
      <div class="brand-square"></div>
      <div class="brand-name">HARBOR LANE</div>
      <div class="brand-sub">ROOM ESCAPE</div>
    </div>
    <div class="cta" style="left:24px;top:558px;width:113px;height:28px;">Read More</div>
  </div>

  <div class="stage-rule bottom"></div>
</div>
</body>
</html>
```